Equipment Finance Specialist I work with companies who need the funds to buy their equipment

I would like a business card that stands out on the shelves. I want to be able to hand it to someone and say WOW. This card should have my logo.
You can put color into it I am very open on design and color

What my company does is we deal with dealerships that sell equipment such as Dump Trucks garbage trucks tractors trailers. Customers get referred to us and depending on their time in business we will ask for the following items

Companies that have been in business for more than two years we have a credit application program up to 250K . With this program we need the following items Credit application filled out(which is what I would like to be able for the customer to click on my website to get.) as well as three current month bank statements.

Deals over 250k we will need the following items

2 years business tax returns
2 years personal tax returns
Profit & Loss statement
Personal Financial Statement

what we do
100% FINANCING
SEASONAL PAYMENTS
LOAN BALLOON PAYMENTS
TRAC LEASING
LOW-INTEREST REFINANCING RATES
DEBT CONSOLIDATION

We specialize in creative financing solutions and offer a variety of reliable, flexible and expandable lending choices.

Target Market(s)

Trucking Companies

Industry/Entity Type

Trucking Company

Contact Information for Business Card

* $250,000 Application only Program
* Loans from $30,000 to 5,000,000
* Competitive Interest Rates

Font styles to use
Serif
Sans Serif

Colors

Designer to choose colors to be used in the design.

Requirements
Must have
• On the back of the card.
• * $250,000 Application only Program
• * Loans from $30,000 to 5,000,000
• My name, email, website. address
• * Competitive Interest Rates
• * 100% Financing
Nice to have
• I want my logo to pop on the card
• My logo is the great one I would like to use
Should not have
• I am up for your creativity as well

```html
<!DOCTYPE html>
<html lang="en">
<head>
<meta charset="utf-8">
<title>Ridgeline Capital – Business Card</title>
<link href="https://fonts.googleapis.com/css2?family=Montserrat:wght@300;400;600;700;800&display=swap" rel="stylesheet">
<style>
  :root {
    --page: #2a2a2a;
    --card-dark: #262626;
    --card-darker: #1c1c1c;
    --panel: #333333;
    --paper: #ffffff;
    --band-light: #e4e4e4;
    --ink: #1d1d1d;
    --ink-soft: #3a3a3a;
    --silver: #e9e9e9;
    --muted: #cfcfcf;
  }
  * { box-sizing: border-box; margin: 0; padding: 0; }
  html, body { width: 1200px; height: 1200px; overflow: hidden; }
  body {
    background: var(--page);
    font-family: "Montserrat", Arial, sans-serif;
    position: relative;
  }
  .card {
    position: absolute;
    left: 170px;
    width: 860px;
    height: 490px;
    overflow: hidden;
    box-shadow: 0 10px 30px rgba(0,0,0,.45);
  }
  /* ---------- back ---------- */
  .card-back { top: 90px; background: var(--paper); }
  .back-top { position: absolute; left: 0; top: 0; width: 100%; height: 48px; background: var(--paper); }
  .back-band {
    position: absolute; left: 0; top: 48px; width: 100%; height: 140px;
    background: var(--card-dark);
  }
  .back-logo-panel {
    position: absolute; left: 250px; top: 30px; width: 360px; height: 180px;
    background: linear-gradient(160deg, #3b3b3b, #202020);
    border: 6px solid var(--paper);
    display: flex; align-items: center; justify-content: center; gap: 12px;
  }
  .brand-dot { width: 34px; height: 34px; border-radius: 50%; background: var(--silver); flex: none; }
  .brand-name {
    color: var(--silver); font-weight: 800; text-transform: uppercase;
    letter-spacing: 1px; line-height: 1;
  }
  .back-logo-panel .brand-name { font-size: 30px; }
  .features {
    position: absolute; left: 40px; top: 240px; list-style: none;
    color: var(--ink); font-size: 21px; font-weight: 300; line-height: 1.55;
  }
  .features li::before {
    content: ""; display: inline-block; width: 10px; height: 10px; border-radius: 50%;
    background: var(--ink); margin-right: 14px; vertical-align: middle;
  }
  .features b { font-weight: 700; }
  .person {
    position: absolute; right: 40px; top: 225px; text-align: right; color: var(--ink);
  }
  .person-name { font-size: 22px; font-weight: 700; }
  .person-title { font-size: 19px; font-weight: 300; color: var(--ink-soft); margin-bottom: 22px; }
  .person-address { font-size: 18px; font-weight: 300; line-height: 1.4; color: var(--ink-soft); }
  .contact-strip {
    position: absolute; left: 0; bottom: 0; width: 100%; height: 58px;
    background: var(--card-dark); color: var(--muted);
    display: flex; align-items: center; justify-content: space-between;
    padding: 0 40px; font-size: 16px; font-weight: 300;
  }
  .contact-item { display: flex; align-items: center; gap: 10px; }
  .contact-item svg { width: 18px; height: 18px; fill: none; stroke: var(--muted); stroke-width: 1.8; }
  /* ---------- front ---------- */
  .card-front { top: 620px; background: var(--card-dark); }
  .front-face {
    position: absolute; left: 0; top: 0; width: 100%; height: 370px;
    background: radial-gradient(ellipse at 50% 45%, #383838, var(--card-darker));
    display: flex; align-items: center; justify-content: center; gap: 22px;
  }
  .front-face .brand-dot { width: 70px; height: 70px; }
  .front-face .brand-name { font-size: 62px; }
  .front-band {
    position: absolute; left: 0; bottom: 0; width: 100%; height: 120px;
    background: var(--band-light);
    display: flex; align-items: center; justify-content: center;
    color: var(--ink); font-size: 40px; font-weight: 700;
  }
</style>
</head>
<body>

<section class="card card-back">
  <div class="back-top"></div>
  <div class="back-band"></div>
  <div class="back-logo-panel">
    <span class="brand-dot"></span>
    <span class="brand-name">Ridgeline Capital</span>
  </div>

  <ul class="features">
    <li><b>$250,000</b> Application only Program</li>
    <li>Loans from <b>$30,000 to 5,000,000</b></li>
    <li>Competitive Interest Rates</li>
    <li><b>100%</b> Financing</li>
  </ul>

  <div class="person">
    <div class="person-name">Your Name</div>
    <div class="person-title">Your Title</div>
    <div class="person-address">Your Address, City<br>State, Zip 0000, Country</div>
  </div>

  <div class="contact-strip">
    <span class="contact-item">
      <svg viewBox="0 0 24 24" aria-hidden="true"><path d="M5 3h4l2 5-2.5 1.5a11 11 0 0 0 6 6L16 13l5 2v4a2 2 0 0 1-2 2A16 16 0 0 1 3 5a2 2 0 0 1 2-2z"/></svg>
      (012) 345 6789
    </span>
    <span class="contact-item">
      <svg viewBox="0 0 24 24" aria-hidden="true"><rect x="3" y="5" width="18" height="14" rx="1"/><path d="M3 6l9 7 9-7"/></svg>
      youremail@mailbox.com
    </span>
    <span class="contact-item">
      <svg viewBox="0 0 24 24" aria-hidden="true"><circle cx="12" cy="12" r="9"/><path d="M3 12h18M12 3c3 3 3 15 0 18M12 3c-3 3-3 15 0 18"/></svg>
      www.yourwebsite.com
    </span>
  </div>
</section>

<section class="card card-front">
  <div class="front-face">
    <span class="brand-dot"></span>
    <span class="brand-name">Ridgeline Capital</span>
  </div>
  <div class="front-band">www.yourwebsite.com</div>
</section>

</body>
</html>
```